Stationery and Biz Cards for a Publishing Solutions Company
Bram Keswick Publishing Solutions, LLC
Simple
Lyle R. Pennock
President/Managing Editor
478 Birchfield Hollow Road
Marlow Ridge, PA 16874
lyle.pennock@bramkeswickbooks.example
www.bramkeswickbooks.example
Here is the company logo.

```html
<!DOCTYPE html>
<html lang="en">
<head>
<meta charset="utf-8">
<title>Bram Keswick Publishing Solutions – Business Card</title>
<link href="https://fonts.googleapis.com/css2?family=Libre+Baskerville:wght@400;700&display=swap" rel="stylesheet">
<style>
  :root {
    --stage: #e9e9ec;
    --royal: #2a2f9a;
    --royal-deep: #151a6b;
    --royal-light: #4a57c9;
    --silver: #b9bcc4;
    --paper: #fbfbfd;
    --ink: #1c2170;
    --ink-soft: #3b3f63;
  }
  html, body {
    margin: 0;
    width: 1200px;
    height: 901px;
    overflow: hidden;
    background: var(--stage);
    font-family: "Libre Baskerville", Georgia, serif;
  }
  .stage {
    position: relative;
    width: 1200px;
    height: 901px;
  }
  .card {
    position: absolute;
    left: 320px;
    width: 560px;
    height: 320px;
    border-radius: 14px;
    overflow: hidden;
    box-shadow: 0 6px 18px rgba(0,0,0,.18);
  }
  /* Back side */
  .card-back {
    top: 90px;
    background: radial-gradient(ellipse at 50% 30%, var(--royal-light), var(--royal) 55%, var(--royal-deep));
    display: flex;
    flex-direction: column;
    align-items: center;
    justify-content: center;
    gap: 22px;
  }
  .brand-mark {
    width: 74px;
    height: 74px;
    border-radius: 8px;
    background: var(--paper);
  }
  .brand-name {
    color: var(--paper);
    font-weight: 400;
    font-size: 26px;
    letter-spacing: 1px;
    text-align: center;
    line-height: 1.25;
    margin: 0;
  }
  /* Front side */
  .card-front {
    top: 490px;
    background: var(--paper);
  }
  .card-front .swoosh {
    position: absolute;
    inset: 0;
  }
  .holder {
    position: absolute;
    right: 22px;
    top: 22px;
    text-align: right;
    color: var(--paper);
  }
  .holder-name {
    margin: 0;
    font-weight: 700;
    font-size: 17px;
  }
  .holder-title {
    margin: 4px 0 0;
    font-size: 12px;
  }
  .front-brand {
    position: absolute;
    left: 30px;
    top: 84px;
    display: flex;
    align-items: center;
    gap: 14px;
  }
  .front-brand .brand-mark {
    width: 46px;
    height: 46px;
    border-radius: 6px;
    background: var(--royal);
  }
  .front-brand .brand-name {
    color: var(--ink);
    font-size: 17px;
    text-align: left;
  }
  .contact {
    position: absolute;
    right: 22px;
    bottom: 22px;
    margin: 0;
    padding: 0;
    list-style: none;
    display: grid;
    grid-template-columns: auto auto;
    gap: 8px 18px;
    font-size: 9.5px;
    color: var(--ink-soft);
  }
  .contact li {
    display: flex;
    align-items: flex-start;
    gap: 6px;
    line-height: 1.35;
    white-space: nowrap;
  }
  .contact .wide { grid-column: 1 / 3; }
  .contact svg { flex: none; width: 11px; height: 11px; fill: var(--royal); }
</style>
</head>
<body>
<main class="stage">
  <section class="card card-back" aria-label="Business card back">
    <div class="brand-mark"></div>
    <p class="brand-name">BRAM KESWICK<br>PUBLISHING SOLUTIONS</p>
  </section>

  <section class="card card-front" aria-label="Business card front">
    <svg class="swoosh" viewBox="0 0 560 320" preserveAspectRatio="none" aria-hidden="true">
      <defs>
        <linearGradient id="swoosh-blue" x1="0" y1="0" x2="1" y2="1">
          <stop offset="0" stop-color="#4a57c9"/>
          <stop offset="1" stop-color="#1a1f78"/>
        </linearGradient>
      </defs>
      <path d="M150,0 C320,70 470,130 560,182 V158 C470,112 320,58 180,0 Z" fill="var(--silver)"/>
      <path d="M180,0 H560 V158 C470,112 320,58 180,0 Z" fill="url(#swoosh-blue)"/>
    </svg>

    <div class="holder">
      <p class="holder-name">Lyle R. Pennock</p>
      <p class="holder-title">President/Managing Editor</p>
    </div>

    <div class="front-brand">
      <div class="brand-mark"></div>
      <p class="brand-name">BRAM KESWICK<br>PUBLISHING SOLUTIONS</p>
    </div>

    <ul class="contact">
      <li>
        <svg viewBox="0 0 12 12"><rect x="1" y="2.5" width="10" height="7" rx="1"/></svg>
        <span>lyle.pennock@bramkeswickbooks.example</span>
      </li>
      <li>
        <svg viewBox="0 0 12 12"><path d="M6 1a3.5 3.5 0 0 1 3.5 3.5C9.5 7.5 6 11 6 11S2.5 7.5 2.5 4.5A3.5 3.5 0 0 1 6 1z"/></svg>
        <span>478 Birchfield Hollow Road<br>Marlow Ridge, PA 16874</span>
      </li>
      <li></li>
      <li>
        <svg viewBox="0 0 12 12"><path d="M3 1h2l1 3-1.5 1a6 6 0 0 0 2.5 2.5L8 6l3 1v2a1.5 1.5 0 0 1-1.5 1.5A8.5 8.5 0 0 1 1.5 2.5 1.5 1.5 0 0 1 3 1z"/></svg>
        <span>555.014.2287</span>
      </li>
      <li class="wide">
        <svg viewBox="0 0 12 12"><circle cx="6" cy="6" r="5"/></svg>
        <span>www.bramkeswickbooks.example</span>
      </li>
    </ul>
  </section>
</main>
</body>
</html>
```